Clean business card with logo provided

I want a card that will stand out among the masses. I need the color and image to show professionalism and yet have a family appeal showing that I only deal with win/win scenarios. The back of the card will be used to take notes about the individual so I can use that in my database entry. I like modern design but need professionalism in it also. It needs to fit my "clean, safe, and affordable housing" motto. I need to be able to write on the file and update the card details for my employees.

Target Market(s)

Investors looking to make investment income through real estate

Industry/Entity Type

Real Estate

Contact Information for Business Card

Troy Vandemark
blank address, city, st, zip code
480-555-0147
troyvandemark@quillrentals.example
www.quillrentals.example

Font styles to use
Sans Serif

Requirements
Must have
• I would like the back of the card to have lines for info. example
• Met/Visited: Date:
• Interets:
Nice to have
• I want the cards color to match the logo background color. Font with details to be san serif and black. I want the card rectangular with square corners. Standard business card size. I would like to see cards designed with both images to see which i prefer more.

```html
<!DOCTYPE html>
<html lang="en">
<head>
<meta charset="utf-8">
<title>Quill Rentals LLC – Business Card</title>
<link rel="stylesheet" href="https://fonts.googleapis.com/css2?family=Open+Sans:wght@400;600&display=swap">
<style>
  :root {
    --canvas: #2a2a2c;
    --card-black: #0b0c0d;
    --card-black-soft: #1b1d1f;
    --paper: #f3f3f3;
    --teal: #1fb5c4;
    --ink: #222222;
    --grey-text: #a9adb0;
    --dots-dark: #555555;
  }
  * { box-sizing: border-box; margin: 0; padding: 0; }
  html, body { width: 1200px; height: 900px; overflow: hidden; }
  body {
    background: var(--canvas);
    font-family: "Open Sans", Arial, sans-serif;
    position: relative;
  }
  .card {
    position: absolute;
    left: 285px;
    width: 630px;
    height: 360px;
  }

  /* Notes side */
  .card-notes {
    top: 50px;
    background: var(--card-black);
    padding: 12px;
  }
  .notes-sheet {
    width: 100%;
    height: 100%;
    background: var(--paper);
    padding: 48px 44px 0 44px;
    color: var(--ink);
    font-size: 19px;
  }
  .note-row {
    display: flex;
    align-items: flex-end;
    height: 46px;
  }
  .note-label { white-space: nowrap; margin-right: 10px; line-height: 1; }
  .note-field-time { margin-left: 18px; }
  .dots {
    flex: 1;
    height: 0;
    border-bottom: 3px dotted var(--teal);
    margin-bottom: 3px;
  }
  .dots-dark { border-bottom-color: var(--dots-dark); }
  .note-row-interests { margin-top: 14px; }
  .note-label-caps { letter-spacing: 0.5px; }

  /* Contact side */
  .card-contact {
    top: 490px;
    background: radial-gradient(ellipse at 40% 30%, var(--card-black-soft), var(--card-black) 70%);
    color: var(--grey-text);
  }
  .brand {
    position: absolute;
    right: 50px;
    top: 58px;
    text-align: right;
  }
  .brand-name {
    display: flex;
    align-items: center;
    justify-content: flex-end;
    gap: 12px;
    color: var(--teal);
    font-weight: 400;
    font-size: 30px;
    letter-spacing: 3px;
  }
  .brand-dot {
    width: 16px; height: 16px;
    border-radius: 50%;
    background: var(--paper);
  }
  .brand-tagline {
    margin-top: 6px;
    color: var(--teal);
    font-size: 12px;
  }
  .divider {
    position: absolute;
    left: 335px;
    right: 0;
    top: 182px;
    height: 1px;
    background: var(--teal);
  }
  .holder-name {
    position: absolute;
    left: 48px;
    top: 160px;
    color: var(--teal);
    font-weight: 600;
    font-size: 30px;
    text-transform: uppercase;
    letter-spacing: 0.5px;
  }
  .contact-list {
    position: absolute;
    left: 50px;
    top: 214px;
    list-style: none;
    font-size: 17px;
  }
  .contact-item {
    display: flex;
    align-items: center;
    height: 28px;
  }
  .contact-icon {
    width: 14px; height: 14px;
    margin-right: 12px;
    fill: var(--teal);
    flex: none;
  }
</style>
</head>
<body>

  <section class="card card-notes" aria-label="Card back for notes">
    <div class="notes-sheet">
      <div class="note-row">
        <span class="note-label">Meet/Visited:</span><span class="dots"></span>
      </div>
      <div class="note-row"><span class="dots"></span></div>
      <div class="note-row">
        <span class="note-label">Date:</span><span class="dots dots-dark"></span>
        <span class="note-label note-field-time">Time:</span><span class="dots"></span>
      </div>
      <div class="note-row"><span class="dots"></span></div>
      <div class="note-row note-row-interests">
        <span class="note-label note-label-caps">INTERETS:</span><span class="dots"></span>
      </div>
      <div class="note-row"><span class="dots"></span></div>
    </div>
  </section>

  <section class="card card-contact" aria-label="Card front with contact details">
    <div class="brand">
      <div class="brand-name"><span class="brand-dot"></span>QUILL RENTALS LLC</div>
      <div class="brand-tagline">Providing clean, safe, and affordable housing</div>
    </div>
    <div class="divider"></div>
    <h1 class="holder-name">Troy Vandemark</h1>
    <ul class="contact-list">
      <li class="contact-item">
        <svg class="contact-icon" viewBox="0 0 16 16"><path d="M3 1l3 0 1 4-2 1c1 2 3 4 5 5l1-2 4 1 0 3c0 1-1 2-2 2C7 15 1 9 1 3c0-1 1-2 2-2z"/></svg>
        480-555-0147
      </li>
      <li class="contact-item">
        <svg class="contact-icon" viewBox="0 0 16 16"><circle cx="8" cy="8" r="6.5" fill="none" stroke="#1fb5c4" stroke-width="1.6"/><path d="M1.5 8h13M8 1.5c-3 3.5-3 9.5 0 13M8 1.5c3 3.5 3 9.5 0 13" fill="none" stroke="#1fb5c4" stroke-width="1.2"/></svg>
        www.quillrentals.example
      </li>
      <li class="contact-item">
        <svg class="contact-icon" viewBox="0 0 16 16"><rect x="1" y="3" width="14" height="10" rx="1"/><path d="M1.5 4l6.5 5 6.5-5" fill="none" stroke="#0b0c0d" stroke-width="1.3"/></svg>
        troyvandemark@quillrentals.example
      </li>
      <li class="contact-item">
        <svg class="contact-icon" viewBox="0 0 16 16"><path d="M8 1a5 5 0 0 1 5 5c0 4-5 9-5 9S3 10 3 6a5 5 0 0 1 5-5z"/><circle cx="8" cy="6" r="2" fill="#0b0c0d"/></svg>
        blank address, city, st, zip code
      </li>
    </ul>
  </section>

</body>
</html>
```